Martial art rank diploma

Need a diploma for a martial arts belt rank . The art is Japanese in origin , traditional is good , stylish , eye catching .
Dragons are good , no cartoon figures . Tacky is not good . Something proud to display
No martial art poses
Must have place for date , head instructor signature

And must say (a blank for students name )
"Having confirmed with all standards and requirements set forth by Brevant Martial Arts and Fitness , is hereby promoted to the rank of " ( a blank for the rank)
Updates

Project Deadline Extended
Reason: nice designs, need to see more to compare

Industry/Entity Type

Martial Art

Requirements
Must have
• Logo attached and name of the school
Nice to have
• Dragon , that does not look like a centipede .

maybe best to have a dragon in the background as a water mark type of thing.
Should not have
• Tacky look or cartoon figures, or any martial art poses

```html
<!DOCTYPE html>
<html lang="en">
<head>
<meta charset="utf-8">
<title>Brevant Martial Arts and Fitness – Rank Diploma</title>
<link href="https://fonts.googleapis.com/css2?family=Source+Sans+3:ital,wght@0,400;0,600;0,700;1,300;1,400&display=swap" rel="stylesheet">
<style>
  :root {
    --paper-top: #ffffff;
    --paper-mid: #fbe3cf;
    --paper-bottom: #f7be93;
    --ink: #2b2b2b;
    --ink-soft: #3a3a3a;
    --brand: #e4622a;
    --figure-dark: #5a2e1c;
    --figure-mid: #b5704a;
    --figure-light: #e7a77c;
    --logo-bg: #ffffff;
  }
  * { box-sizing: border-box; margin: 0; padding: 0; }
  html, body { width: 935px; height: 1200px; overflow: hidden; }
  body { font-family: "Source Sans 3", "Myriad Pro", sans-serif; color: var(--ink); }

  .diploma {
    position: relative;
    width: 935px;
    height: 1200px;
    overflow: hidden;
    background: linear-gradient(180deg, var(--paper-top) 0%, var(--paper-mid) 45%, var(--paper-bottom) 100%);
  }

  .hero-art {
    position: absolute;
    left: 0;
    top: 20px;
    width: 560px;
    height: 1180px;
  }

  .school-mark {
    position: absolute;
    left: 397px;
    top: 17px;
    width: 369px;
    height: 122px;
    background: var(--logo-bg);
    display: flex;
    align-items: center;
    justify-content: center;
    gap: 14px;
  }
  .school-mark__dot {
    width: 34px; height: 34px;
    border-radius: 50%;
    background: var(--brand);
    flex: none;
  }
  .school-mark__name {
    font-weight: 700;
    color: var(--brand);
    font-size: 25px;
    line-height: 1.05;
  }

  .title {
    position: absolute;
    left: 566px;
    top: 128px;
    font-size: 104px;
    font-style: italic;
    font-weight: 300;
    letter-spacing: -2px;
    color: var(--ink);
    line-height: 1;
  }

  .recipient {
    position: absolute;
    left: 537px;
    top: 264px;
    width: 384px;
    display: flex;
    align-items: flex-end;
    font-weight: 700;
    font-size: 19px;
  }
  .recipient__blank {
    flex: 1;
    border-bottom: 1.5px solid var(--ink);
    margin-left: 2px;
    height: 20px;
  }

  .citation {
    position: absolute;
    left: 535px;
    top: 315px;
    width: 392px;
    text-align: center;
    font-style: italic;
    font-size: 20px;
    line-height: 32px;
    color: var(--ink-soft);
  }

  .rank-blank {
    position: absolute;
    left: 543px;
    top: 492px;
    width: 375px;
    border-bottom: 1.5px solid var(--ink);
  }

  .quote {
    position: absolute;
    left: 283px;
    top: 936px;
    font-style: italic;
    font-size: 27px;
    color: var(--ink-soft);
    white-space: nowrap;
  }
  .quote__author {
    position: absolute;
    left: 616px;
    top: 981px;
    font-style: italic;
    font-size: 27px;
    color: var(--ink-soft);
  }

  .dated {
    position: absolute;
    left: 458px;
    top: 1047px;
    font-style: italic;
    font-size: 19px;
    color: var(--ink-soft);
    white-space: nowrap;
  }
  .dated__blank {
    display: inline-block;
    border-bottom: 1.2px solid var(--ink);
    vertical-align: baseline;
    height: 1px;
  }
  .dated__blank--day { width: 38px; }
  .dated__blank--month { width: 128px; }

  .signature {
    position: absolute;
    left: 766px;
    top: 1155px;
    width: 118px;
    border-top: 1px solid var(--ink);
    text-align: center;
    padding-top: 4px;
    font-style: italic;
    font-size: 12.5px;
    color: var(--ink-soft);
  }
</style>
</head>
<body>
<main class="diploma">
  <svg class="hero-art" viewBox="0 0 560 1180" role="img" aria-label="Photograph of a martial artist figurine in a high-kick stance, shown in warm brown tones">
    <defs>
      <radialGradient id="figureGlow" cx="0.42" cy="0.45" r="0.62">
        <stop offset="0" stop-color="var(--figure-mid)" stop-opacity="0.85"/>
        <stop offset="0.55" stop-color="var(--figure-dark)" stop-opacity="0.55"/>
        <stop offset="1" stop-color="var(--figure-light)" stop-opacity="0"/>
      </radialGradient>
    </defs>
    <rect x="0" y="0" width="560" height="1180" fill="url(#figureGlow)"/>
  </svg>

  <div class="school-mark">
    <span class="school-mark__dot"></span>
    <span class="school-mark__name">Brevant<br>Martial Arts &amp; Fitness</span>
  </div>

  <h1 class="title">Diploma</h1>

  <div class="recipient">To:<span class="recipient__blank"></span></div>

  <p class="citation">Having confirmed with all standards and requirements set forth by Brevant Martial Arts and Fitness , is hereby promoted to the rank of</p>

  <div class="rank-blank"></div>

  <p class="quote">“Perceive that which cannot be seen with the eye.”</p>
  <p class="quote__author">Kaito Arisawa</p>

  <p class="dated">Dated this <span class="dated__blank dated__blank--day"></span> day of <span class="dated__blank dated__blank--month"></span>,2013</p>

  <div class="signature">Head instructor</div>
</main>
</body>
</html>
```